Film Poster For Short Thriller

UPDATE:

The original concept seemed to be a bit difficult for designers to source elements, so we're changing our brief.

Please use the biohazard symbol (attached for reference only, please use any source file for this symbol you would like) in the middle of the poster. In the top 1/3 please place "Plim" in large font with "A Doran Kelvitch Film" in smaller font underneath it. All text should be centered.

What we would like to see with this simplified design is something that's eye-catching but simple and elegant. There should be interesting detail (e.g. texture added to the biohazard symbol, an interesting but not distracting background).

What the design is and what it needs is extremely simple and fully laid out above. We're looking for someone who can take a simple idea (which on the face of it is also simple to execute) and add something memorable. Thank you!
Updates

Hello all, and thank you for your interest in this project. It seems that the original brief was difficult to execute without better source images. The brief has been updated in a way that we believe will be much easier for graphic designers to create an impactful poster. Thank you!

Target Market(s)

Film festivals, online promotion, Strella Reel On Demand

Colors
0255a3
fbee3e

Requirements
Must have
• The dimensions will be 24” width, 40” height, and high enough PPI to be printed at that size. I would think that would 300 PPI, but if you have other thoughts please let me know.

```html
<!DOCTYPE html>
<html lang="en">
<head>
<meta charset="utf-8">
<title>Plim – A Doran Kelvitch Film</title>
<link href="https://fonts.googleapis.com/css2?family=Rubik+Dirt&family=Rubik:wght@700&display=swap" rel="stylesheet">
<style>
  :root {
    --ink: #f4f4f2;
    --night: #0b0b0d;
    --steel: #5a5d63;
    --suit-violet: #6a5fe0;
    --suit-deep: #3a2fb8;
    --hood-yellow: #f2e12a;
    --hazard-yellow: #fbee3e;
    --hazard-edge: #1a1a1f;
  }
  html, body {
    margin: 0;
    padding: 0;
    width: 867px;
    height: 1200px;
    background: var(--night);
    overflow: hidden;
  }
  .poster {
    position: relative;
    width: 867px;
    height: 1200px;
    overflow: hidden;
    background: var(--night);
  }
  .facility-scene {
    position: absolute;
    inset: 0;
    background:
      radial-gradient(ellipse at 50% 55%, rgba(158,162,168,0.35) 0%, rgba(90,93,99,0.25) 35%, rgba(11,11,13,0) 70%),
      linear-gradient(180deg, var(--night) 0%, #1c1d20 30%, var(--steel) 62%, #2a2b2e 100%);
  }
  .hazmat-figure {
    position: absolute;
    left: 128px;
    top: 496px;
    width: 616px;
    height: 704px;
    background:
      radial-gradient(ellipse 42% 30% at 50% 22%, rgba(242,225,42,0.85) 0%, rgba(242,225,42,0) 100%),
      radial-gradient(ellipse 60% 75% at 50% 75%, var(--suit-violet) 0%, var(--suit-deep) 60%, rgba(58,47,184,0) 100%);
  }
  .hazard-symbol {
    position: absolute;
    left: 283px;
    top: 560px;
    width: 300px;
    height: 300px;
  }
  .title-block {
    position: absolute;
    top: 88px;
    left: 0;
    width: 100%;
    text-align: center;
    color: var(--ink);
  }
  .film-title {
    margin: 0;
    font-family: "Rubik Dirt", "Arial Black", sans-serif;
    font-size: 170px;
    line-height: 152px;
    font-weight: 400;
    letter-spacing: 8px;
    padding-left: 36px;
  }
  .film-credit {
    margin: 44px 0 0;
    font-family: "Rubik", "Arial Black", sans-serif;
    font-size: 29px;
    font-weight: 700;
    letter-spacing: 4px;
    padding-left: 36px;
  }
</style>
</head>
<body>
  <main class="poster">
    <div class="facility-scene" role="img" aria-label="Dim industrial plant interior with overhead ducts, pipes and steel walkways"></div>
    <div class="hazmat-figure" role="img" aria-label="Figure in a violet protective suit with a yellow hood and visor, head bowed"></div>
    <svg class="hazard-symbol" viewBox="-50 -50 100 100" aria-label="Biohazard symbol">
      <defs>
        <mask id="hazard-cut">
          <rect x="-50" y="-50" width="100" height="100" fill="#000"/>
          <g fill="#fff">
            <circle cx="0" cy="-22" r="24"/>
            <circle cx="19.05" cy="11" r="24"/>
            <circle cx="-19.05" cy="11" r="24"/>
          </g>
          <circle cx="0" cy="0" r="17" fill="none" stroke="#fff" stroke-width="5"/>
          <g fill="#000">
            <circle cx="0" cy="-29" r="17"/>
            <circle cx="25.11" cy="14.5" r="17"/>
            <circle cx="-25.11" cy="14.5" r="17"/>
            <circle cx="0" cy="0" r="6"/>
          </g>
          <g stroke="#000" stroke-width="2.4">
            <line x1="0" y1="0" x2="0" y2="-14"/>
            <line x1="0" y1="0" x2="12.1" y2="7"/>
            <line x1="0" y1="0" x2="-12.1" y2="7"/>
          </g>
        </mask>
      </defs>
      <rect x="-50" y="-50" width="100" height="100" fill="var(--hazard-yellow)" mask="url(#hazard-cut)"/>
    </svg>
    <header class="title-block">
      <h1 class="film-title">PLIM</h1>
      <p class="film-credit">A DORAN KELVITCH FILM</p>
    </header>
  </main>
</body>
</html>
```